Ketwinall Need to look more professional with our Word Press design

I need to change the look of our Word Press site. Must haves- Newsletter option, contact page refer to www.ketwinall.com.au

Industry/Entity Type

It Professional

```html
<!DOCTYPE html>
<html lang="en">
<head>
<meta charset="utf-8">
<title>Ketwinall – Key Account Management Services</title>
<link href="https://fonts.googleapis.com/css2?family=Lato:ital,wght@0,300;0,400;0,700;1,400&family=Lora:ital,wght@0,400;0,700;1,400&display=swap" rel="stylesheet">
<style>
:root{
  --ink:#222222;
  --text:#444444;
  --muted:#666666;
  --white:#ffffff;
  --black:#0b0b0b;
  --band:#3b3b3b;
  --light:#f1f1f1;
  --gold:#f5c218;
  --gold-line:#e7b400;
}
*{box-sizing:border-box;margin:0;padding:0}
html,body{width:1200px;height:4124px;overflow:hidden}
body{font-family:'Lato',sans-serif;color:var(--text);background:var(--white);position:relative}
section,header,footer{position:relative;width:1200px}
.photo{position:absolute;display:block}

/* hero */
.hero{height:660px;background:#2a2118}
.hero .photo{inset:0;background:radial-gradient(ellipse at 45% 40%,#5a4530 0%,#3a2c1f 45%,#1c1610 100%)}
.hero-shade{position:absolute;inset:0;background:rgba(0,0,0,.25)}
.nav{position:absolute;top:0;left:0;right:0;height:90px;display:flex;align-items:center;justify-content:space-between;padding:0 44px}
.brand{display:flex;align-items:center;gap:10px;color:var(--white);font-weight:700;font-size:22px}
.brand-dot{width:16px;height:16px;border-radius:50%;background:var(--gold)}
.menu{display:flex;gap:28px;list-style:none}
.menu li{color:var(--white);font-size:19px}
.menu li.active{border-bottom:2px solid var(--white);padding-bottom:4px}
.hero-copy{position:absolute;top:268px;left:0;right:0;text-align:center;color:var(--white)}
.hero-copy h1{font-weight:400;font-size:62px;letter-spacing:.5px}
.hero-copy p{font-size:17px;line-height:26px;width:640px;margin:18px auto 0}
.btn-ghost{display:inline-block;margin-top:26px;border:2px solid var(--white);color:var(--white);font-size:18px;padding:12px 30px}

/* newsletter */
.newsletter{height:268px;background:var(--band);color:var(--white)}
.newsletter h2{position:absolute;left:91px;top:736px;top:74px;font-weight:400;font-size:30px}
.newsletter p{position:absolute;left:91px;top:122px;width:640px;font-size:15px;line-height:23px;color:#dddddd}
.field{position:absolute;left:928px;top:78px;width:239px;height:42px;background:var(--white);color:#888;font-size:14px;padding:12px 14px}
.btn-sub{position:absolute;left:928px;top:134px;width:239px;height:46px;border:2px solid var(--white);color:var(--white);font-size:19px;text-align:center;line-height:42px}

/* intro */
.intro{height:235px;background:var(--light);text-align:center}
.intro h2{padding-top:58px;font-weight:400;font-size:32px;color:var(--ink)}
.intro p{width:880px;margin:18px auto 0;font-size:16px;line-height:23px;color:var(--muted)}

.strip-title{height:115px;background:var(--black);color:var(--white);text-align:center;font-size:30px;line-height:115px;font-weight:400}
.gallery{height:227px;display:flex}
.gallery .photo{position:relative;height:227px}

/* features */
.features{height:640px;display:flex;gap:49px;padding:62px 91px 0}
.feature{width:306px}
.feature-head{display:flex;align-items:center;gap:12px;font-size:19px;color:var(--ink);height:30px}
.feature .photo{position:relative;width:306px;height:206px;margin-top:18px}
.feature h3{text-align:center;font-weight:400;font-size:21px;color:var(--ink);margin-top:22px}
.feature p{text-align:center;font-size:15px;line-height:22px;margin-top:10px;color:var(--muted)}

/* banner */
.banner{height:350px;color:var(--white);text-align:center}
.banner .photo{inset:0;background:radial-gradient(circle at 30% 40%,#6d6f78 0%,#3a3c44 40%,#15171c 100%)}
.banner-copy{position:absolute;top:128px;left:0;right:0}
.banner h2{font-weight:400;font-size:38px}
.banner p{width:920px;margin:16px auto 0;font-size:16px;line-height:24px}

/* articles */
.articles{height:701px;display:flex;gap:60px;padding:80px 91px 0}
.article{width:479px}
.article h2{font-weight:400;font-size:34px;color:var(--ink)}
.article p{font-size:15.5px;line-height:23.5px;margin-top:18px;color:var(--muted)}
.btn-read{position:absolute;top:572px;display:block;border:2px solid var(--gold);color:var(--gold);font-size:17px;width:104px;height:44px;text-align:center;line-height:40px}

/* testimonials */
.testimonials{height:598px;background:var(--black)}
.testimonials h2{text-align:center;color:var(--white);font-family:'Lora',serif;font-weight:400;font-size:32px;padding-top:52px}
.cards{position:absolute;top:268px;left:91px;display:flex;gap:49px}
.card{width:310px;height:268px;background:var(--gold);text-align:center;color:var(--ink);padding-top:66px;position:relative}
.avatar{position:absolute;top:-34px;left:120px;width:70px;height:70px;border-radius:50%;border:4px solid var(--white);background:linear-gradient(135deg,#b48a6a,#6a4d3a)}
.card p{font-size:15px;line-height:22px;width:250px;margin:0 auto}
.card .who{margin-top:18px;font-weight:700}
.card .role{font-size:14px;margin-top:2px}

/* quote */
.quote{height:268px;display:flex;align-items:center}
.quote blockquote{margin-left:91px;border-left:6px solid var(--gold-line);padding:6px 0 6px 34px;font-family:'Lora',serif;font-style:italic;font-size:25px;line-height:38px;color:var(--ink);width:1010px}

.site-footer{height:62px;background:var(--black);color:#bbbbbb;font-size:13px;letter-spacing:1px;padding:24px 0 0 91px}
</style>
</head>
<body>

<header class="hero">
  <div class="photo" role="img" aria-label="Overhead photo of a dark wooden table with a cutting board, spices and bowls"></div>
  <div class="hero-shade"></div>
  <nav class="nav">
    <div class="brand"><span class="brand-dot"></span>Ketwinall</div>
    <ul class="menu"><li class="active">Home</li><li>Portfolio</li><li>Contact</li></ul>
  </nav>
  <div class="hero-copy">
    <h1>Key Account Management Services</h1>
    <p>Lorem ipsum dolor sit amet, consectetur adipiscing elit. Morbi dignissim sem non justo sagittis mattis. Nullam nec nulla laoreet, sollicitudin felis.</p>
    <span class="btn-ghost">Learn More</span>
  </div>
</header>

<section class="newsletter">
  <h2>Subscribe to our Newsletter</h2>
  <p>Lorem ipsum dolor sit amet, consectetur adipiscing elit. Morbi dignissim sem non justo sagittis mattis. Nullam nec sollicitudin felis. Donec tristique dignissim leo.</p>
  <div class="field">Email Address</div>
  <div class="btn-sub">Subscribe Now</div>
</section>

<section class="intro">
  <h2>Lorem ipsum dolor sit amet, consectetur adipiscing elit.</h2>
  <p>Lorem ipsum dolor sit amet, consectetur adipiscing elit. Fusce vitae dui et orci porta blandit. Phasellus pretium consectetur ipsum. Vivamus consequat sagittis sem, ac accumsan turpis laoreet eu. Proin mattis fermentum enim, a mollis dui varius eget. Suspendisse potenti. Pellentesque vel maximus eros.</p>
</section>

<section class="strip-title">Lorem ipsum dolor sit amet, consectetur</section>

<section class="gallery">
  <div class="photo" style="width:258px;background:linear-gradient(160deg,#8a9a5a,#4d5a2c)" role="img" aria-label="Deer standing in a green forest clearing"></div>
  <div class="photo" style="width:322px;background:linear-gradient(160deg,#6f7d3c,#3d4520)" role="img" aria-label="Deer grazing in a meadow"></div>
  <div class="photo" style="width:300px;background:linear-gradient(160deg,#6d6a78,#2e2c38)" role="img" aria-label="Bare winter branches against a muted sky"></div>
  <div class="photo" style="width:320px;background:linear-gradient(160deg,#8b7a5e,#3e3426)" role="img" aria-label="Young deer among branches"></div>
</section>

<section class="features">
  <div class="feature">
    <div class="feature-head"><svg width="22" height="22" viewBox="0 0 22 22"><rect x="3" y="3" width="16" height="16" fill="none" stroke="#222" stroke-width="2"/><rect x="7" y="7" width="8" height="8" fill="#222"/></svg>Lorem ipsum dolor sit amet</div>
    <div class="photo" style="background:linear-gradient(135deg,#6b4a2e,#2a1d12)" role="img" aria-label="Wooden cutting board on a dark table"></div>
    <h3>Title</h3>
    <p>Lorem ipsum dolor sit amet, consectetur adipiscing elit. Fusce vitae dui et orci porta blandit. Phasellus pretium consectetur ipsum. Vivamus consequat sagittis sem, ac accumsan turpis laoreet eu. Proin mattis fermentum enim, a mollis dui varius eget. Suspendisse potenti. Pellentesque vel maximus eros. Donec commodo ligula risus, vitae vulputate odio bibendum in.</p>
  </div>
  <div class="feature">
    <div class="feature-head"><svg width="22" height="22" viewBox="0 0 22 22"><path d="M11 2v12M5 9l6 7 6-7" fill="none" stroke="#222" stroke-width="2.5"/><rect x="4" y="18" width="14" height="2" fill="#222"/></svg>Lorem ipsum dolor sit amet</div>
    <div class="photo" style="background:linear-gradient(135deg,#4a4036,#1c1814)" role="img" aria-label="Bowls of spices and herbs on a table"></div>
    <h3>Title</h3>
    <p>Lorem ipsum dolor sit amet, consectetur adipiscing elit. Fusce vitae dui et orci porta blandit. Phasellus pretium consectetur ipsum. Vivamus consequat sagittis sem, ac accumsan turpis laoreet eu. Proin mattis fermentum enim, a mollis dui varius eget. Suspendisse potenti. Pellentesque vel maximus eros. Donec commodo ligula risus, vitae vulputate odio bibendum in.</p>
  </div>
  <div class="feature">
    <div class="feature-head"><svg width="22" height="22" viewBox="0 0 22 22"><circle cx="11" cy="11" r="8.5" fill="none" stroke="#222" stroke-width="2"/><circle cx="11" cy="11" r="3.5" fill="#222"/></svg>Lorem ipsum dolor sit amet</div>
    <div class="photo" style="background:linear-gradient(135deg,#5a4a3a,#201a14)" role="img" aria-label="Cooking ingredients and utensils seen from above"></div>
    <h3>Title</h3>
    <p>Lorem ipsum dolor sit amet, consectetur adipiscing elit. Fusce vitae dui et orci porta blandit. Phasellus pretium consectetur ipsum. Vivamus consequat sagittis sem, ac accumsan turpis laoreet eu. Proin mattis fermentum enim, a mollis dui varius eget. Suspendisse potenti. Pellentesque vel maximus eros. Donec commodo ligula risus, vitae vulputate odio bibendum in.</p>
  </div>
</section>

<section class="banner">
  <div class="photo" role="img" aria-label="Blurred night lights and bare tree branches"></div>
  <div class="banner-copy">
    <h2>Lorem ipsum dolor sit amet, consectetur adipiscing elit</h2>
    <p>Lorem ipsum dolor sit amet, consectetur adipiscing elit. Fusce vitae dui et orci porta blandit. Phasellus pretium consectetur ipsum. Vivamus consequat sagittis sem, ac accumsan turpis laoreet eu. Proin mattis fermentum enim, a mollis dui varius eget. Donec commodo ligula risus, vitae vulputate odio bibendum in. Phasellus pellentesque nibh et sapien suscipit efficitur. Maecenas eget tellus sollicitudin, mollis sem sed, finibus ex. Mauris erat orci, sagittis sed dolor lobortis.</p>
  </div>
</section>

<section class="articles">
  <div class="article">
    <h2>Lorem ipsum dolor sit amet</h2>
    <p>Consectetur adipiscing elit. Fusce vitae dui et orci porta blandit. Phasellus pretium consectetur ipsum. Vivamus consequat sagittis sem, ac accumsan turpis laoreet eu. Proin mattis fermentum enim, a mollis dui varius eget. Suspendisse potenti. Pellentesque vel maximus eros. Donec commodo ligula risus, vitae vulputate odio bibendum in. Phasellus pellentesque nibh et sapien suscipit efficitur. Maecenas eget tellus sollicitudin, mollis sem sed, finibus ex. Mauris erat orci, sagittis sed dolor lobortis, venenatis posuere ex. Consectetur adipiscing elit. Fusce vitae dui et orci porta blandit. Phasellus pretium consectetur ipsum. Vivamus consequat sagittis sem, ac accumsan turpis laoreet eu. Proin mattis fermentum enim, a mollis dui varius eget. Suspendisse potenti. Pellentesque vel maximus eros.</p>
    <span class="btn-read" style="left:91px">Read More</span>
  </div>
  <div class="article">
    <h2>Lorem ipsum dolor sit amet</h2>
    <p>Consectetur adipiscing elit. Fusce vitae dui et orci porta blandit. Phasellus pretium consectetur ipsum. Vivamus consequat sagittis sem, ac accumsan turpis laoreet eu. Proin mattis fermentum enim, a mollis dui varius eget. Suspendisse potenti. Pellentesque vel maximus eros. Donec commodo ligula risus, vitae vulputate odio bibendum in. Phasellus pellentesque nibh et sapien suscipit efficitur. Maecenas eget tellus sollicitudin, mollis sem sed, finibus ex. Mauris erat orci, sagittis sed dolor lobortis, venenatis posuere ex. Consectetur adipiscing elit. Fusce vitae dui et orci porta blandit. Phasellus pretium consectetur ipsum. Vivamus consequat sagittis sem, ac accumsan turpis laoreet eu. Proin mattis fermentum enim, a mollis dui varius eget. Suspendisse potenti. Pellentesque vel maximus eros.</p>
    <span class="btn-read" style="left:630px">Read More</span>
  </div>
</section>

<section class="testimonials">
  <h2>What Our Clients Say About Us</h2>
  <div class="cards">
    <div class="card"><div class="avatar" role="img" aria-label="Client portrait"></div><p>Lorem ipsum dolor sit amet, consectetur adipiscing elit. Fusce vitae dui et orci porta blandit. Phasellus pretium consectetur ipsum.</p><div class="who">Name</div><div class="role">Job title, Company</div></div>
    <div class="card"><div class="avatar" role="img" aria-label="Client portrait"></div><p>Lorem ipsum dolor sit amet, consectetur adipiscing elit. Fusce vitae dui et orci porta blandit. Phasellus pretium consectetur ipsum.</p><div class="who">Name</div><div class="role">Job title, Company</div></div>
    <div class="card"><div class="avatar" role="img" aria-label="Client portrait"></div><p>Lorem ipsum dolor sit amet, consectetur adipiscing elit. Fusce vitae dui et orci porta blandit. Phasellus pretium consectetur ipsum.</p><div class="who">Name</div><div class="role">Job title, Company</div></div>
  </div>
</section>

<section class="quote">
  <blockquote>“Ketwinall is now successfully established in Western Australia. We are thrilled to represent the following, dynamic companies within the Foodservice, Bakery Route and Food Manufactures channels.”</blockquote>
</section>

<footer class="site-footer">COPYRIGHT © 2015-2016 | WEBSITE</footer>

</body>
</html>
```